super clean and modern easy to read. Scandinavian type design.

Hi everyone, we need a wall menu for our retail space. We'd like something that goes along with the style of our website and is also editable (in case we change prices later on). The dimensions for the menu will be about 72 inches wide and about 48 inches high and it will be attached to the wall in our business. Please pull menu wording from this link: http://www.lunaskinloft.example/services

Feel free to shorten the descriptions.

The main sections of the menu are:
luna facials
enhancements
add-ons ($15, $20, and $30)
celebrity facials

Please include the picture of the woman on our homepage in the menu. I'll attach an image.

We would like to start with our process to simplify the steps we take.
1.)Complimentary skin analysis
2.) Choose your service
3.) Choose your products (recommendations are given)
4.) Enjoy!
5.) Further your results with take home products

Last little note, we can email you a larger Logo...Pixel Guild would not let us upload the largest file that we have for the logo.

Target Market(s)

young, fun, hip, suburban women and men.

Industry/Entity Type

Retail

Font styles to use
Sans Serif

Requirements
Must have
• Not too much orange. Keep it clean and not too busy.
• the menu should make it super easy for someone to walk into the store and figure out the process.
• the 5 steps should be listed out first
• the 2 basic facials
• the add ons
• the enhancements (by price)
• the celebrity facials
• Advanced peels
• colors should be mainly blue and white (website) some orange used for framing categories or black. I like clean and not too busy. no cheesy.
Nice to have
• see colors on website. see style.
Should not have
• no clip art! no cursive formal writing.

```html
<!DOCTYPE html>
<html lang="en">
<head>
<meta charset="utf-8">
<title>luna skin loft – service menu</title>
<link href="https://fonts.googleapis.com/css2?family=Roboto+Condensed:wght@400;500&family=Roboto:wght@400;500;700&family=Arimo:wght@400;700&display=swap" rel="stylesheet">
<style>
  :root{
    --teal:#5bc5d3;
    --teal-pale:#d6eff3;
    --orange:#f08a24;
    --ink:#1d1d1d;
    --grey:#555;
    --white:#ffffff;
  }
  *{box-sizing:border-box;margin:0;padding:0}
  html,body{width:1200px;height:814px;overflow:hidden;background:var(--white)}
  .menu{position:relative;width:1200px;height:814px;overflow:hidden;
    background:linear-gradient(100deg,#eef8fa 0%,#ffffff 30%,#ffffff 62%,var(--teal-pale) 100%);
    font-family:"Arimo",Arial,sans-serif;color:var(--ink)}

  /* process band */
  .steps{position:absolute;left:0;top:0;width:1200px;height:130px;background:var(--teal)}
  .step-num{position:absolute;top:36px;width:60px;height:60px;border-radius:50%;background:var(--orange);
    color:var(--white);font:500 36px/60px "Roboto Condensed",sans-serif;text-align:center}
  .step-label{position:absolute;color:var(--white);font:500 29px/1.08 "Roboto Condensed",sans-serif;letter-spacing:-.6px;white-space:nowrap}
  .step-label.tight{font-size:27px;line-height:1.05}

  /* section headings */
  .heading{position:absolute;font:500 38px/1 "Roboto",sans-serif;color:var(--teal);letter-spacing:-.8px;
    white-space:nowrap;padding-bottom:6px;background:
    repeating-linear-gradient(90deg,var(--orange) 0 9px,transparent 9px 14px) left bottom/ calc(100% - 60px) 2px no-repeat}
  .heading .dots{display:inline-block;margin-left:8px;vertical-align:middle}
  .heading .dots i{display:inline-block;width:22px;height:22px;border-radius:50%;background:var(--orange);margin-right:1px}

  .list{position:absolute;list-style:none;font-size:13px;line-height:15px}
  .list li{position:relative;padding-left:10px}
  .list li::before{content:"•";position:absolute;left:0;top:0}
  .list b{font-weight:700}
  .list .note{color:var(--grey)}

  .facial-title{position:absolute;font:700 15.5px/1 "Arimo",sans-serif;white-space:nowrap}
  .facial-list{font-size:12.5px;line-height:13.5px}
  .facial-list li{margin-bottom:2px}
  .series{position:absolute;font:700 14.5px/1 "Arimo",sans-serif}

  .enh-list{font-size:14px;line-height:20.5px}
  .enh-list .wrap{line-height:17px;padding-bottom:3px}
  .addon-list{font-size:13.5px;line-height:16px}
  .addon-list li{margin-bottom:2px}

  .arrow{position:absolute;width:60px;height:60px}

  /* brand */
  .rule{position:absolute;height:2px;background:var(--teal)}
  .brand{position:absolute;left:363px;top:434px;width:417px;text-align:center;
    font:700 70px/1 "Roboto",sans-serif;color:var(--teal);letter-spacing:-3px}

  /* celebrity box */
  .celebrity{position:absolute;left:40px;top:563px;width:743px;height:208px;border:3px solid var(--orange)}
  .celeb-col{position:absolute;top:54px}
  .celeb-col h3{font:700 14px/16px "Arimo",sans-serif}
  .celeb-col .who{font-size:13.5px;line-height:15px;margin-bottom:2px}
  .celeb-col p{font-size:10.5px;line-height:12px;color:var(--grey)}
  .divider{position:absolute;top:58px;width:2px;height:128px;background:var(--orange)}
</style>
</head>
<body>
<main class="menu">

  <header class="steps">
    <div class="step-num" style="left:20px">1.</div>
    <div class="step-label" style="left:86px;top:46px">choose your<br>facial</div>
    <div class="step-num" style="left:240px">2.</div>
    <div class="step-label" style="left:309px;top:48px">complimentary<br>skin analysis</div>
    <div class="step-num" style="left:486px">3.</div>
    <div class="step-label tight" style="left:557px;top:36px">choose<br>products +<br>enhancements</div>
    <div class="step-num" style="left:723px">4.</div>
    <div class="step-label" style="left:795px;top:48px">relax +<br>enjoy!</div>
    <div class="step-num" style="left:883px">5.</div>
    <div class="step-label" style="left:951px;top:46px">extend results with<br>take home products</div>
  </header>

  <!-- luna facials -->
  <h2 class="heading" style="left:35px;top:148px">luna facials<span class="dots"><i></i><i></i></span></h2>
  <div class="facial-title" style="left:35px;top:207px">luna essential 30 min | $49</div>
  <ul class="list facial-list" style="left:35px;top:227px;width:275px">
    <li>deep breathing with lavender essential oils</li>
    <li>includes in-depth skin analysis, with recommendations</li>
    <li>power cleanse x2, hot steam, exfoliation, high frequency treatment or facial vacuum</li>
    <li>shiatsu style massage</li>
    <li>lavender hot towel</li>
    <li>customized mask, sun protection and lip treatment</li>
  </ul>
  <div class="series" style="left:44px;top:369px">Series of 3 | $125</div>
  <div class="facial-title" style="left:35px;top:393px">luna advanced 45 min | $69</div>
  <ul class="list facial-list" style="left:35px;top:420px;width:285px">
    <li>includes the essential facial + a more advanced and customized treatment</li>
    <li>extractions, deeper cleansing, exfoliation and hydration</li>
    <li>lymphatic massage, neck massage, a hand, arm and décolleté massage</li>
  </ul>
  <div class="series" style="left:44px;top:507px">Series of 3 | $170</div>

  <!-- arrows -->
  <svg class="arrow" style="left:326px;top:253px" viewBox="0 0 60 60" aria-hidden="true">
    <circle cx="30" cy="30" r="30" fill="var(--orange)"/>
    <path d="M24 17 L37 30 L24 43" fill="none" stroke="#fff" stroke-width="7"/>
  </svg>
  <svg class="arrow" style="left:694px;top:253px" viewBox="0 0 60 60" aria-hidden="true">
    <circle cx="30" cy="30" r="30" fill="var(--orange)"/>
    <path d="M24 17 L37 30 L24 43" fill="none" stroke="#fff" stroke-width="7"/>
  </svg>

  <!-- enhancements -->
  <h2 class="heading" style="left:389px;top:148px">enhancements $10<span class="dots"><i></i><i></i></span></h2>
  <ul class="list enh-list" style="left:430px;top:210px;width:290px">
    <li><b>vitamin c</b> <span class="note">(radiance + fine lines)</span></li>
    <li><b>peptide (</b><span class="note">plump + smooth)</span></li>
    <li class="wrap"><b>hyaluronic acid</b><br><span class="note">(moisture + anti-aging)</span></li>
    <li><b>retinol</b> <span class="note">(fine lines + age spots)</span></li>
    <li><b>dehydrated eye treatment</b></li>
    <li class="wrap"><b>cherry enzyme peel</b><br><span class="note">(antioxidant + healthy glow)</span></li>
    <li><b>pumpkin</b> <span class="note">(revitalizes + reduces lines)</span></li>
  </ul>

  <!-- brand -->
  <div class="rule" style="left:363px;top:401px;width:417px"></div>
  <div class="brand">luna skin loft</div>
  <div class="rule" style="left:363px;top:540px;width:417px"></div>

  <!-- add-ons -->
  <h2 class="heading" style="left:818px;top:148px">add-ons $15<span class="dots"><i></i><i></i></span></h2>
  <ul class="list addon-list" style="left:818px;top:207px;width:370px">
    <li><b>wax - brow, chin or lip</b> <span class="note">(touch up)</span></li>
    <li><b>magnetic mud mask</b><br><span class="note">(nourish + mineral infusion)</span></li>
    <li><b>peppermint/eucalyptus scalp massage</b><br><span class="note">(invigorating + stress reduction)</span></li>
    <li><b>beard oil treatment</b><br><span class="note">(softens + protects)</span></li>
  </ul>

  <h2 class="heading" style="left:818px;top:335px">add-ons $20<span class="dots"><i></i><i></i></span></h2>
  <ul class="list addon-list" style="left:818px;top:393px;width:375px">
    <li><b>me time - 20 min extra massage</b><span class="note">(relax + enjoy)</span></li>
    <li><b>hand rejuvenation peel or microderm</b><br><span class="note">(exfoliating + anti-aging)</span></li>
  </ul>

  <h2 class="heading" style="left:818px;top:453px">add-ons $30<span class="dots"><i></i><i></i></span></h2>
  <ul class="list addon-list" style="left:818px;top:510px;width:360px">
    <li><b>crystal microdermabrasion for face and neck or décolleté - 2 passes</b> <span class="note">(fine lines + smoothing)</span></li>
    <li><b>diamond microdermabrasion for face and neck or décolleté - 2 passes</b> <span class="note">(fine lines + smoothing)</span></li>
    <li><b>led light therapy - 20 min</b> <span class="note">(red for anti-aging) (blue for acne)</span></li>
    <li><b>décolleté treatment</b><br><span class="note">(peel or microderm) (anti-aging + fine lines)</span></li>
    <li><b>whole face wax</b> <span class="note">(except brows)</span></li>
    <li><b>hand treatment - peel + microderm</b><br><span class="note">(double exfoliation for anti-aging)</span></li>
    <li><b>facial hydration cocktail -1 pass of microderm + 7 advanced serums to fully hydrate your skin</b> <span class="note">(glow + renew)</span></li>
    <li><b>microcurrent eye, mouth, or chin</b> <span class="note">(non-surgical face lift)</span></li>
  </ul>

  <!-- celebrity facials -->
  <section class="celebrity">
    <h2 class="heading" style="left:194px;top:8px">celebrity facials<span class="dots"><i></i><i></i></span></h2>

    <div class="celeb-col" style="left:20px;width:138px">
      <h3>oxygen facial<br>50 min | $130</h3>
      <div class="who">(mara lee's secret to red carpet skin)</div>
      <p>hydrates and plumps. hyaluronic and peptide serums are infused into the skin with oxygen for an instant glow.</p>
    </div>
    <div class="divider" style="left:168px"></div>

    <div class="celeb-col" style="left:184px;width:142px">
      <h3>led therapy facial<br>50 min | $130</h3>
      <div class="who">(delia hart's fav)</div>
      <p>we use LED for anti-aging, correcting discoloration, healing acne, and reversing the effects of sun damage. LED has been FDA approved for beauty treatments.</p>
    </div>
    <div class="divider" style="left:331px"></div>

    <div class="celeb-col" style="left:346px;width:160px">
      <h3>Lumo Non Surgical facelift | 50 min | $130</h3>
      <div class="who">(renata cruz)</div>
      <p>non-surgical facelift. microcurrent works by re-training the muscles in the face to reverse the effects of aging. ask about details and package pricing.</p>
    </div>
    <div class="divider" style="left:517px"></div>

    <div class="celeb-col" style="left:533px;width:205px">
      <h3>50 min | micro + peel | $130</h3>
      <p>the microderm and peel combo combines 2 advanced treatments into one. microderm will help the peel penetrate to a deeper level.</p>
      <h3 style="margin-top:10px">50 min advanced peel | $130</h3>
      <p>Advanced peels go deep in your skin to reverse sun damage, wrinkles, acne and signs of aging.</p>
    </div>
  </section>

</main>
</body>
</html>
```